Mobile Recording Studio needs business cards

Open to seeing a creative design, but I want to emphasis my logo and minimize the name/title and company information. Possible a fully black background on card.

My company is a mobile sound recording studio. ok to include a my trailer (actual or cartoon) on the card. My initial thought is more straight forward, but a good design will win me over.

SPECS:
CMYK color mode
High (300ppi) raster effect.
cover bleed area
please deliver: Illustrator file with layers and a pdf at completion.

Name and info for the business card:

Dallin Perry
ADR Mixer

email: Dallin@MixVault.com

address:
248 - 5170 East Hollister
Vancouver, BC V5R 2J4

phone:
604.518.2093 office

website:
www.MixVault.com

FB: @MixVault

Instagram: @TheMixVault

Industry/Entity Type

Television Production

Contact Information for Business Card

Dallin Perry
ADR Mixer

email: Dallin@MixVault.com

address:
248 - 5170 East Hollister
Vancouver, BC V5R 2J4

phone:
604.518.2093 office

website:
www.MixVault.com

FB: @MixVault

Instagram: @TheMixVault

Colors

Designer to choose colors to be used in the design.

Requirements
Must have
• emphasis my logo and minimize the name/title and company information.
• SPECS:
• CMYK color mode
• High (300ppi) raster effect.
• cover bleed area
• please deliver: Illustrator file with layers and a pdf at completion.
Nice to have
• maybe include the following:
• all black background or black theme
• my work trailer (actual or cartoon) refer to Instagram: @TheMixVault

```html
<!DOCTYPE html>
<html lang="en">
<head>
<meta charset="utf-8">
<title>MixVault Business Card</title>
<link href="https://fonts.googleapis.com/css2?family=Cinzel:wght@600&family=Montserrat:wght@400;600&display=swap" rel="stylesheet">
<style>
  :root {
    --backdrop: #1f2023;
    --card: #0b0b0c;
    --silver: #cfd0d2;
    --text: #e6e6e6;
    --muted: #b9b9bb;
    --rule: #8d8e91;
  }
  * { box-sizing: border-box; margin: 0; padding: 0; }
  html, body {
    width: 1200px; height: 900px; overflow: hidden;
    background: var(--backdrop);
  }
  .sheet {
    width: 1200px; height: 900px;
    display: flex; align-items: center; justify-content: center; gap: 50px;
  }
  .card {
    width: 525px; height: 300px;
    background: var(--card);
    border-radius: 4px;
    position: relative;
    box-shadow: 0 10px 30px rgba(0,0,0,.45);
  }
  .brand-name {
    font-family: "Cinzel", serif;
    font-weight: 600;
    color: var(--silver);
    letter-spacing: 0.02em;
    line-height: 1;
  }
  /* front */
  .card-front { display: flex; align-items: center; justify-content: center; }
  .card-front .brand-name { font-size: 66px; }
  /* back */
  .card-back { display: flex; align-items: center; padding: 0 28px; }
  .back-brand { width: 170px; display: flex; justify-content: center; }
  .back-brand .brand-name { font-size: 28px; }
  .divider { width: 1px; height: 230px; background: var(--rule); margin: 0 24px 0 14px; }
  .details { font-family: "Montserrat", sans-serif; color: var(--text); font-size: 11px; line-height: 1.55; }
  .person-name {
    font-family: "Cinzel", serif; font-weight: 600;
    font-size: 15px; letter-spacing: 0.06em; color: var(--text);
  }
  .person-title { color: var(--muted); font-size: 10.5px; }
  .dash { width: 10px; height: 1px; background: var(--text); margin: 10px 0 12px; }
  .web { font-weight: 600; margin-bottom: 8px; }
  .address { margin-bottom: 8px; }
  .socials { display: flex; gap: 22px; }
  .social { display: flex; align-items: center; gap: 6px; }
  .social-dot { width: 10px; height: 10px; border-radius: 50%; background: var(--text); }
</style>
</head>
<body>
  <main class="sheet">
    <section class="card card-front" aria-label="Card front">
      <span class="brand-name">MixVault</span>
    </section>

    <section class="card card-back" aria-label="Card back">
      <div class="back-brand"><span class="brand-name">MixVault</span></div>
      <div class="divider"></div>
      <div class="details">
        <p class="person-name">DALLIN PERRY</p>
        <p class="person-title">Engineer / Director of Operations</p>
        <div class="dash"></div>
        <p class="phone">Office: 604.518.2093</p>
        <p class="web">www.MixVault.com</p>
        <p class="address">248 - 5170 East Hollister<br>Vancouver, BC V5R 2J4</p>
        <div class="socials">
          <span class="social"><span class="social-dot"></span>@MixVault</span>
          <span class="social"><span class="social-dot"></span>@TheMixVault</span>
        </div>
      </div>
    </section>
  </main>
</body>
</html>
```